Design of a carbonated cola drink

our competitor is selling brimhaven cola
their design is en closed
we need a similar design colours but we cant use
brimhaven cola
we were thinking of usuing
the words VRO cola
using a bit of the american flag colors red and blue
designs for three flavors shown below should be shown
the main drink colour is zimp red
orange lurvo orange
punch like brevoni /glimmer fizz

Target Market(s)

pacific islands

Requirements
Must have
• mentioned above
Nice to have
• mentioned above

```html
<!DOCTYPE html>
<html lang="en">
<head>
<meta charset="utf-8">
<title>VRO cola – flavour can labels</title>
<link rel="stylesheet" href="https://fonts.googleapis.com/css2?family=Roboto:wght@400;700&display=swap">
<style>
  :root {
    --backdrop: #1f0306;
    --label-white: #ffffff;
    --flag-blue: #1d4f8c;
    --flag-blue-light: #5f86b8;
    --dot-blue: #2d66b3;
    --name-grey: #3a3a3a;

    --cola-main: #e0101e;
    --cola-dark: #b30d1a;
    --cola-soft: #f07a6a;
    --cola-pale: #f6b6ac;

    --orange-main: #f57c00;
    --orange-dark: #d35400;
    --orange-soft: #ffb24d;
    --orange-pale: #ffd9a3;

    --punch-main: #c2187a;
    --punch-dark: #8e0f5a;
    --punch-soft: #ef6fb4;
    --punch-pale: #f8bcdc;
  }
  html, body {
    margin: 0;
    width: 1200px;
    height: 1016px;
    overflow: hidden;
    background: var(--backdrop);
  }
  .canvas {
    position: relative;
    width: 1200px;
    height: 1016px;
  }
  .can-label {
    position: absolute;
    top: 183px;
    width: 300px;
    height: 650px;
    display: block;
  }
  .can-label--cola { left: 75px; }
  .can-label--orange { left: 450px; }
  .can-label--punch { left: 825px; }

  .label-base { fill: var(--label-white); }
  .star-stop-top { stop-color: var(--flag-blue-light); }
  .star-stop-base { stop-color: var(--flag-blue); }
  .dot-stop { stop-color: var(--dot-blue); }

  .can-label--cola { --swoosh-main: var(--cola-main); --swoosh-dark: var(--cola-dark); --swoosh-soft: var(--cola-soft); --swoosh-pale: var(--cola-pale); }
  .can-label--orange { --swoosh-main: var(--orange-main); --swoosh-dark: var(--orange-dark); --swoosh-soft: var(--orange-soft); --swoosh-pale: var(--orange-pale); }
  .can-label--punch { --swoosh-main: var(--punch-main); --swoosh-dark: var(--punch-dark); --swoosh-soft: var(--punch-soft); --swoosh-pale: var(--punch-pale); }

  .swoosh { fill: none; }
  .swoosh--dark { stroke: var(--swoosh-dark); }
  .swoosh--main { stroke: var(--swoosh-main); }
  .swoosh--soft { stroke: var(--swoosh-soft); }
  .swoosh--pale { stroke: var(--swoosh-pale); }

  .brand-name {
    font-family: "Roboto", Arial, sans-serif;
    font-weight: 700;
    font-size: 104px;
    fill: var(--name-grey);
  }
  .top-tag {
    font-family: "Roboto", Arial, sans-serif;
    font-weight: 400;
    font-size: 14px;
    fill: var(--flag-blue);
  }
</style>
</head>
<body>
<main class="canvas">

  <svg class="can-label can-label--cola" viewBox="0 0 360 780" xmlns="http://www.w3.org/2000/svg" aria-label="VRO cola label, cola flavour">
    <defs>
      <linearGradient id="stars-cola" x1="0" y1="0" x2="0" y2="1">
        <stop offset="0" class="star-stop-top"/>
        <stop offset="0.5" class="star-stop-base"/>
        <stop offset="1" class="star-stop-base"/>
      </linearGradient>
      <linearGradient id="dots-cola" x1="0" y1="0" x2="1" y2="1">
        <stop offset="0" class="dot-stop" stop-opacity="0.55"/>
        <stop offset="0.6" class="dot-stop" stop-opacity="0.15"/>
        <stop offset="1" class="dot-stop" stop-opacity="0"/>
      </linearGradient>
    </defs>
    <rect class="label-base" width="360" height="780"/>
    <path role="img" aria-label="Blue halftone dot pattern fading into white" d="M170 0 H360 V470 C300 420 230 360 200 240 C185 160 175 80 170 0 Z" fill="url(#dots-cola)"/>
    <path role="img" aria-label="Blue flag band with scattered white stars" d="M0 0 H95 C100 220 90 420 70 780 H0 Z" fill="url(#stars-cola)"/>
    <g>
      <path class="swoosh swoosh--dark" d="M95 0 C100 260 120 560 240 780" stroke-width="36"/>
      <path class="swoosh swoosh--main" d="M125 0 C125 280 150 560 270 780" stroke-width="34"/>
      <path class="swoosh swoosh--soft" d="M150 0 C150 300 175 580 290 780" stroke-width="12"/>
      <path class="swoosh swoosh--pale" d="M163 0 C163 310 190 590 305 780" stroke-width="6"/>
      <path class="swoosh swoosh--main" d="M80 0 C80 280 95 560 200 780" stroke-width="10" opacity="0.8"/>
    </g>
    <text class="top-tag" x="150" y="34">VRO cola</text>
    <text class="brand-name" transform="translate(258 560) rotate(-90)">VRO cola</text>
  </svg>

  <svg class="can-label can-label--orange" viewBox="0 0 360 780" xmlns="http://www.w3.org/2000/svg" aria-label="VRO cola label, orange flavour">
    <defs>
      <linearGradient id="stars-orange" x1="0" y1="0" x2="0" y2="1">
        <stop offset="0" class="star-stop-top"/>
        <stop offset="0.5" class="star-stop-base"/>
        <stop offset="1" class="star-stop-base"/>
      </linearGradient>
      <linearGradient id="dots-orange" x1="0" y1="0" x2="1" y2="1">
        <stop offset="0" class="dot-stop" stop-opacity="0.55"/>
        <stop offset="0.6" class="dot-stop" stop-opacity="0.15"/>
        <stop offset="1" class="dot-stop" stop-opacity="0"/>
      </linearGradient>
    </defs>
    <rect class="label-base" width="360" height="780"/>
    <path role="img" aria-label="Blue halftone dot pattern fading into white" d="M170 0 H360 V470 C300 420 230 360 200 240 C185 160 175 80 170 0 Z" fill="url(#dots-orange)"/>
    <path role="img" aria-label="Blue flag band with scattered white stars" d="M0 0 H95 C100 220 90 420 70 780 H0 Z" fill="url(#stars-orange)"/>
    <g>
      <path class="swoosh swoosh--dark" d="M95 0 C100 260 120 560 240 780" stroke-width="36"/>
      <path class="swoosh swoosh--main" d="M125 0 C125 280 150 560 270 780" stroke-width="34"/>
      <path class="swoosh swoosh--soft" d="M150 0 C150 300 175 580 290 780" stroke-width="12"/>
      <path class="swoosh swoosh--pale" d="M163 0 C163 310 190 590 305 780" stroke-width="6"/>
      <path class="swoosh swoosh--main" d="M80 0 C80 280 95 560 200 780" stroke-width="10" opacity="0.8"/>
    </g>
    <text class="top-tag" x="150" y="34">VRO cola</text>
    <text class="brand-name" transform="translate(258 560) rotate(-90)">VRO cola</text>
  </svg>

  <svg class="can-label can-label--punch" viewBox="0 0 360 780" xmlns="http://www.w3.org/2000/svg" aria-label="VRO cola label, punch flavour">
    <defs>
      <linearGradient id="stars-punch" x1="0" y1="0" x2="0" y2="1">
        <stop offset="0" class="star-stop-top"/>
        <stop offset="0.5" class="star-stop-base"/>
        <stop offset="1" class="star-stop-base"/>
      </linearGradient>
      <linearGradient id="dots-punch" x1="0" y1="0" x2="1" y2="1">
        <stop offset="0" class="dot-stop" stop-opacity="0.55"/>
        <stop offset="0.6" class="dot-stop" stop-opacity="0.15"/>
        <stop offset="1" class="dot-stop" stop-opacity="0"/>
      </linearGradient>
    </defs>
    <rect class="label-base" width="360" height="780"/>
    <path role="img" aria-label="Blue halftone dot pattern fading into white" d="M170 0 H360 V470 C300 420 230 360 200 240 C185 160 175 80 170 0 Z" fill="url(#dots-punch)"/>
    <path role="img" aria-label="Blue flag band with scattered white stars" d="M0 0 H95 C100 220 90 420 70 780 H0 Z" fill="url(#stars-punch)"/>
    <g>
      <path class="swoosh swoosh--dark" d="M95 0 C100 260 120 560 240 780" stroke-width="36"/>
      <path class="swoosh swoosh--main" d="M125 0 C125 280 150 560 270 780" stroke-width="34"/>
      <path class="swoosh swoosh--soft" d="M150 0 C150 300 175 580 290 780" stroke-width="12"/>
      <path class="swoosh swoosh--pale" d="M163 0 C163 310 190 590 305 780" stroke-width="6"/>
      <path class="swoosh swoosh--main" d="M80 0 C80 280 95 560 200 780" stroke-width="10" opacity="0.8"/>
    </g>
    <text class="top-tag" x="150" y="34">VRO cola</text>
    <text class="brand-name" transform="translate(258 560) rotate(-90)">VRO cola</text>
  </svg>

</main>
</body>
</html>
```